Text heavy poster for university audience

I have developed a set of standards for online teaching that need to be turned into a post format. The project has a logo which should be incorporated. Most of the designing will be in terms of text layout. The logo (two versions - higher quality files available) and the a sample of standards (as image - word version available; the example is one third of standards) are attached. Design that can be adapted to brochure format would be great. (Brochure adaption will be paid separately via another project to be opened here). More details available here: http://www.brightmeadowhub.org
Updates

Dear all,

The URL for the site needs to be include in the design - either as footer or under logo:
<http://www.brightmeadowhub.org>

Sorry for late notice

Target Market(s)

The are university staff

Industry/Entity Type

University

Font styles to use
Serif
Sans Serif

Requirements
Must have
• The text in the "required" attachment must be included; but for initial draft feel free to restrict your design to "sample" attachment
The green from the Logo (PANTONE 17-5641 Emerald) should be the foundation of the colour palette.
Nice to have
• The collaborators as named here: http://www.brightmeadowhub.org/collaborators/
My preferred find is helvetica neue, but similar can be used
Should not have
• Decorative fonts

```html
<!DOCTYPE html>
<html lang="en">
<head>
<meta charset="utf-8">
<title>Bright Meadow Teaching Standards – Poster</title>
<link href="https://fonts.googleapis.com/css2?family=Roboto:wght@300;400;700;900&family=Roboto+Condensed:wght@400;700&display=swap" rel="stylesheet">
<style>
:root{
  --emerald:#2f9a6e;
  --emerald-deep:#1f7a55;
  --emerald-dark:#17513a;
  --mint:#bfe3d1;
  --mint-light:#dff1e8;
  --mint-pale:#eef8f3;
  --ink:#1c3d30;
  --white:#ffffff;
  --label:#2c8c63;
  --row-good:#3fa27a;
  --row-threshold:#a9d9c2;
}
*{box-sizing:border-box;margin:0;padding:0}
html,body{width:848px;height:1200px;overflow:hidden}
body{font-family:"Roboto","Helvetica Neue",Arial,sans-serif;color:var(--ink)}
.poster{position:relative;width:848px;height:1200px;overflow:hidden;
  background:linear-gradient(180deg,var(--emerald) 0%,#5db891 12%,#a6d6bf 30%,#c7e6d6 50%,#a9d8c1 75%,#4fae86 90%,var(--emerald-deep) 100%)}

/* header */
.masthead{position:absolute;left:0;top:0;width:848px;height:170px}
.brand{position:absolute;left:30px;top:86px;display:flex;align-items:center;gap:12px}
.brand-mark{width:54px;height:54px;border-radius:50%;background:var(--white)}
.brand-name{font-family:"Roboto Condensed","Helvetica Neue",sans-serif;font-weight:700;font-size:17px;line-height:20px;color:var(--white);letter-spacing:.5px}
.icon-cluster{position:absolute;left:300px;top:10px;width:250px;height:110px;border-radius:55px;
  background:radial-gradient(ellipse at center,rgba(255,255,255,.28),rgba(255,255,255,0) 70%)}
.licence{position:absolute;left:600px;top:50px;width:225px;color:var(--white)}
.licence-name{display:flex;align-items:center;gap:6px;font-weight:700;font-size:15px;margin-bottom:6px}
.licence-name span.dot{width:18px;height:18px;border-radius:50%;border:2px solid var(--white)}
.licence p{font-size:6.4px;line-height:8.6px}

/* panels */
.panel{position:absolute;left:28px;width:792px;background:var(--white);border-radius:10px;padding:6px 10px 8px}
.panel-head{display:flex;align-items:center;justify-content:center;gap:12px;height:28px;margin-bottom:4px}
.panel-head h2{font-weight:900;font-size:19px;letter-spacing:.5px;color:var(--emerald-dark)}
.panel-head p{font-size:6.6px;line-height:8.4px;width:190px;color:var(--ink)}
.students{top:172px;height:275px}
.staff{top:458px;height:125px}
.organisation{top:594px;height:206px}
.collaborators{top:812px;height:262px}

.cols{display:grid;grid-template-columns:1fr 1fr 1fr;gap:14px}
.col{display:flex;flex-direction:column;gap:5px}
.col.offset{padding-top:22px}

.standard{display:block}
.standard h3{display:flex;align-items:flex-start;gap:6px;font-family:"Roboto Condensed","Helvetica Neue",sans-serif;font-weight:700;font-size:7.2px;line-height:8.4px;color:var(--emerald-dark);min-height:18px;padding-top:2px}
.standard h3 .num{font-family:"Roboto",sans-serif;font-weight:300;font-size:19px;line-height:16px;color:var(--emerald)}
.levels{display:grid;grid-template-columns:40px 1fr;gap:1px;background:var(--white);border-radius:3px;overflow:hidden}
.levels dt{background:var(--label);color:var(--white);font-weight:700;font-size:6.2px;padding:0 5px;display:flex;align-items:center}
.levels dd{font-size:6.2px;line-height:7.4px;padding:3px 6px;min-height:15px;display:flex;align-items:center}
.levels dd.threshold{background:var(--row-threshold);color:var(--ink)}
.levels dd.good{background:var(--row-good);color:var(--white)}
.levels dd.excellent{background:var(--mint-pale);min-height:12px}

/* collaborators */
.collaborators .panel-head h2{font-size:17px}
.names{display:grid;grid-template-columns:repeat(6,1fr);gap:0 10px;padding:0 8px}
.names ul{list-style:none}
.names li{font-size:7px;line-height:10.9px;color:var(--ink);white-space:nowrap}

/* footer */
.footer{position:absolute;left:0;top:1086px;width:848px;height:114px;background:var(--emerald-deep);color:var(--white);display:flex;align-items:center;padding:0 30px}
.footer .brand-name{font-size:14px;line-height:16px}
.footer .brand-mark{width:40px;height:40px}
.footer-brand{display:flex;align-items:center;gap:10px;width:190px}
.partner{display:flex;align-items:center;gap:8px;width:140px;border-left:1px solid rgba(255,255,255,.5);padding-left:12px}
.partner-mark{width:26px;height:26px;background:var(--white)}
.partner p{font-size:7.5px;line-height:10px}
.partner strong{display:block;font-size:9px;font-weight:700}
.contact{width:140px;padding-left:14px}
.contact strong{display:block;font-size:12px;font-weight:700}
.contact span{display:block;font-size:7.5px;line-height:11px}
.site{margin-left:auto;font-weight:700;font-size:15px;color:var(--white);text-decoration:none}
</style>
</head>
<body>
<main class="poster">

<header class="masthead">
  <div class="icon-cluster" role="img" aria-label="Cluster of small learning and technology icons"></div>
  <div class="brand">
    <span class="brand-mark"></span>
    <div class="brand-name">BRIGHT MEADOW<br>TEACHING<br>STANDARDS</div>
  </div>
  <div class="licence">
    <div class="licence-name"><span class="dot"></span>Shared Works Licence</div>
    <p>This work is licensed under the Shared Works Attribution-ShareAlike 3.0 Unported Licence. To view a copy of this licence, visit http://www.brightmeadowhub.org/licence or send a letter to Shared Works Licence, 12 Larch Road, Suite 40, Fernvale, 30218.<br>Support for this activity has been provided by the National Office for Tertiary Teaching. The views expressed in this activity do not necessarily reflect the views of the National Office for Tertiary Teaching.</p>
  </div>
</header>

<section class="panel students">
  <div class="panel-head">
    <h2>STUDENTS</h2>
    <p>Students are supported in their online learning with a quality curriculum [1-3], opportunities for interaction with peers and staff [5&amp;6], and appropriate support [7&amp;8].</p>
  </div>
  <div class="cols">
    <div class="col">
      <article class="standard"><h3><span class="num">1</span>CURRICULUM MATERIALS ARE ALIGNED, AVAILABLE AND ENGAGING</h3>
        <dl class="levels"><dt>Threshold</dt><dd class="threshold">The necessary materials are constructively aligned and available online</dd><dt>Good</dt><dd class="good">The materials are provided using a variety of media to engage students and support diversity</dd><dt>Excellent</dt><dd class="excellent"></dd></dl></article>
      <article class="standard"><h3><span class="num">2</span>LEARNING ACTIVITIES ARE ALIGNED, AVAILABLE AND ENGAGING</h3>
        <dl class="levels"><dt>Threshold</dt><dd class="threshold">Constructively aligned learning activities are available online</dd><dt>Good</dt><dd class="good">Learning activities use a variety of appropriate technologies to engage students and support diversity</dd><dt>Excellent</dt><dd class="excellent"></dd></dl></article>
      <article class="standard"><h3><span class="num">3</span>ASSESSMENT TASKS ARE ALIGNED, AVAILABLE AND ENGAGING</h3>
        <dl class="levels"><dt>Threshold</dt><dd class="threshold">Constructively aligned assessment tasks are available online</dd><dt>Good</dt><dd class="good">Assessment tasks use a variety of appropriate technologies to engage students and support diversity</dd><dt>Excellent</dt><dd class="excellent"></dd></dl></article>
    </div>
    <div class="col">
      <article class="standard"><h3><span class="num">4</span>STUDENTS ARE PROVIDED WITH TIMELY, IMPROVEMENT FOCUSED FORMATIVE FEEDBACK</h3>
        <dl class="levels"><dt>Threshold</dt><dd class="threshold">Appropriate technologies are used to provide students with formative feedback in a timely manner</dd><dt>Good</dt><dd class="good">Feedback is provided in a variety of media to engage students and support diversity</dd><dt>Excellent</dt><dd class="excellent"></dd></dl></article>
      <article class="standard"><h3><span class="num">5</span>STUDENTS ARE PROVIDED WITH OPPORTUNITIES TO INTERACT WITH PEERS</h3>
        <dl class="levels"><dt>Threshold</dt><dd class="threshold">There are opportunities for student-student interaction</dd><dt>Good</dt><dd class="good">There are opportunities for learning-focused interaction</dd><dt>Excellent</dt><dd class="excellent"></dd></dl></article>
      <article class="standard"><h3><span class="num">6</span>STUDENTS ARE PROVIDED WITH OPPORTUNITIES TO INTERACT WITH STAFF</h3>
        <dl class="levels"><dt>Threshold</dt><dd class="threshold">Staff are provided with opportunities to answer student queries</dd><dt>Good</dt><dd class="good">Staff are provided with opportunities to be active participants in learning-focused interactions</dd><dt>Excellent</dt><dd class="excellent"></dd></dl></article>
    </div>
    <div class="col offset">
      <article class="standard"><h3><span class="num">7</span>STUDENTS ARE PROVIDED WITH APPROPRIATE LEARNING SUPPORT</h3>
        <dl class="levels"><dt>Threshold</dt><dd class="threshold">Appropriate, up-to-date and reliable learning guides and resources are provided online</dd><dt>Good</dt><dd class="good">A range of appropriate, up-to-date and reliable online learning skills workshops are available</dd><dt>Excellent</dt><dd class="excellent"></dd></dl></article>
      <article class="standard"><h3><span class="num">8</span>STUDENTS ARE SUPPORTED IN THEIR USE OF EDUCATIONAL TECHNOLOGY</h3>
        <dl class="levels"><dt>Threshold</dt><dd class="threshold">Appropriate, up-to-date and reliable technological guides and resources are provided online</dd><dt>Good</dt><dd class="good">Appropriate, timely and reliable asynchronous technological support is available</dd><dt>Excellent</dt><dd class="excellent"></dd></dl></article>
    </div>
  </div>
</section>

<section class="panel staff">
  <div class="panel-head">
    <h2>STAFF</h2>
    <p>Staff are supported in their online teaching with quality professional development [9], resourcing [10] and technical support [11].</p>
  </div>
  <div class="cols">
    <article class="standard"><h3><span class="num">9</span>STAFF ARE PROVIDED WITH QUALITY PROFESSIONAL DEVELOPMENT IN ONLINE EDUCATION</h3>
      <dl class="levels"><dt>Threshold</dt><dd class="threshold">A range of appropriate, up-to-date and innovative professional development activities are available to staff</dd><dt>Good</dt><dd class="good">The organisation requires staff to engage in continued professional development relevant to online education</dd><dt>Excellent</dt><dd class="excellent"></dd></dl></article>
    <article class="standard"><h3><span class="num">10</span>ONLINE EDUCATION IS RECOGNISED IN WORKLOAD</h3>
      <dl class="levels"><dt>Threshold</dt><dd class="threshold">Online teaching is recognised in workload</dd><dt>Good</dt><dd class="good">Online and development is recognised in workload</dd><dt>Excellent</dt><dd class="excellent"></dd></dl></article>
    <article class="standard"><h3><span class="num">11</span>STAFF ARE SUPPORTED IN THEIR USE OF EDUCATIONAL TECHNOLOGY</h3>
      <dl class="levels"><dt>Threshold</dt><dd class="threshold">Appropriate, up-to-date and reliable technological guides and resources are provided online</dd><dt>Good</dt><dd class="good">Appropriate, timely and reliable asynchronous technological support is available</dd><dt>Excellent</dt><dd class="excellent"></dd></dl></article>
  </div>
</section>

<section class="panel organisation">
  <div class="panel-head">
    <h2>ORGANISATION</h2>
    <p>Staff are supported in their online teaching with quality professional development [9], resourcing [10] and technical support [11].</p>
  </div>
  <div class="cols">
    <div class="col">
      <article class="standard"><h3><span class="num">12</span>THE ORGANISATION PROVIDES STRATEGIC LEADERSHIP IN ONLINE EDUCATION</h3>
        <dl class="levels"><dt>Threshold</dt><dd class="threshold">The organisation has a clearly articulated strategic position on online education</dd><dt>Good</dt><dd class="good">An appropriate member of the executive has explicit responsibility for online education</dd><dt>Excellent</dt><dd class="excellent"></dd></dl></article>
      <article class="standard"><h3><span class="num">13</span>THE ORGANISATION EMPLOYS A SYSTEMATIC APPROACH TO RESOURCE ALLOCATION IN ONLINE EDUCATION</h3>
        <dl class="levels"><dt>Threshold</dt><dd class="threshold">There is a systematic approach to resource allocation</dd><dt>Good</dt><dd class="good">There is a systematic approach with formal criteria that are widely available</dd><dt>Excellent</dt><dd class="excellent"></dd></dl></article>
    </div>
    <div class="col">
      <article class="standard"><h3><span class="num">14</span>THE ORGANISATION MAINTAINS AND SUPPORTS A QUALITY LEARNING PLATFORM FOR DELIVERING ONLINE EDUCATION</h3>
        <dl class="levels"><dt>Threshold</dt><dd class="threshold">The organisation maintains and supports an appropriate learning platform</dd><dt>Good</dt><dd class="good">The learning platform provided is fit for purpose, scalable and reliable</dd><dt>Excellent</dt><dd class="excellent"></dd></dl></article>
      <article class="standard"><h3><span class="num">15</span>THE ORGANISATION HAS A PROCESS FOR EVALUATING AND IMPROVING STUDENT SATISFACTION WITH ONLINE EDUCATION</h3>
        <dl class="levels"><dt>Threshold</dt><dd class="threshold">The organisation has a systematic process for evaluating and improving student satisfaction with online education</dd><dt>Good</dt><dd class="good">The organisation has a systematic process for improving student learning outcomes and satisfaction and communicating improvements to students</dd><dt>Excellent</dt><dd class="excellent"></dd></dl></article>
    </div>
    <div class="col">
      <article class="standard"><h3><span class="num">16</span>THE ORGANISATION HAS A PROCESS FOR EVALUATING AND IMPROVING TRAINING AND SUPPORT FOR STAFF</h3>
        <dl class="levels"><dt>Threshold</dt><dd class="threshold">The organisation has a systematic process for evaluating and improving staff training and support</dd><dt>Good</dt><dd class="good">The organisation has a systematic process for improving staff training and support and communicating improvements to staff</dd><dt>Excellent</dt><dd class="excellent"></dd></dl></article>
      <article class="standard"><h3><span class="num">17</span>THE ORGANISATION HAS A PROCESS FOR EVALUATING AND IMPROVING INFRASTRUCTURE</h3>
        <dl class="levels"><dt>Threshold</dt><dd class="threshold">The organisation has a systematic process for evaluating and improving infrastructure</dd><dt>Good</dt><dd class="good">The organisation has a systematic process for improving infrastructure and communicating improvements to stakeholders</dd><dt>Excellent</dt><dd class="excellent"></dd></dl></article>
    </div>
  </div>
</section>

<section class="panel collaborators">
  <div class="panel-head"><h2>COLLABORATORS</h2></div>
  <div class="names">
    <ul><li>Abbott, Lena (NGU)</li><li>Ackland, Tom (Eastvale)</li><li>Alden, Priya (NGU)</li><li>Ambrose, Kit (Coastal)</li><li>Archer, Mei (Ridge Uni)</li><li>Ashby, Noel (NGU)</li><li>Baird, Iris (Eastvale)</li><li>Barlow, Sam (Westmere)</li><li>Baxter, Joy (NGU)</li><li>Bellamy, Ray (Coastal)</li><li>Benton, Ada (Ridge Uni)</li><li>Blake, Hugo (NGU)</li><li>Bond, Lucia (Eastvale)</li><li>Brennan, Otto (Westmere)</li><li>Brooks, Tess (NGU)</li><li>Burke, Ivan (Coastal)</li><li>Byrne, Cora (NGU)</li><li>Calder, Finn (Ridge Uni)</li><li>Carver, Nina (Eastvale)</li><li>Chase, Leo (NGU)</li></ul>
    <ul><li>Clarke, Ruth (NGU)</li><li>Colby, Dean (Westmere)</li><li>Connor, Aria (Coastal)</li><li>Crane, Miles (NGU)</li><li>Dalton, Eve (Eastvale)</li><li>Darcy, Jude (Ridge Uni)</li><li>Dawes, Flora (NGU)</li><li>Dixon, Paul (Coastal)</li><li>Doyle, Nora (NGU)</li><li>Drake, Cyrus (Westmere)</li><li>Dunn, Hazel (Eastvale)</li><li>Eaton, Rhys (NGU)</li><li>Ellis, Maya (Ridge Uni)</li><li>Emery, Grant (NGU)</li><li>Farrell, Zoe (Coastal)</li><li>Fenwick, Ali (NGU)</li><li>Fielding, Rose (Eastvale)</li><li>Finch, Owen (Westmere)</li><li>Fleming, Ana (NGU)</li><li>Ford, Elliot (Ridge Uni)</li></ul>
    <ul><li>Foster, June (NGU)</li><li>Gale, Aaron (Coastal)</li><li>Garner, Ivy (NGU)</li><li>Gibson, Luke (Eastvale)</li><li>Gordon, Mira (NGU)</li><li>Grady, Neil (Ridge Uni)</li><li>Hale, Sofia (Westmere)</li><li>Hardy, Ben (NGU)</li><li>Harlow, Tara (Coastal)</li><li>Hayes, Colin (NGU)</li><li>Holt, Lara (Eastvale)</li><li>Hughes, Ken (NGU)</li><li>Irving, Dana (Ridge Uni)</li><li>Jarvis, Reid (NGU)</li><li>Keane, Ella (Westmere)</li><li>Kemp, Victor (NGU)</li><li>Kerr, Alma (Coastal)</li><li>Lang, Felix (NGU)</li><li>Lawson, Gina (Eastvale)</li><li>Lowe, Adam (NGU)</li></ul>
    <ul><li>Lyle, Bea (NGU)</li><li>Marsh, Oscar (Coastal)</li><li>Mason, Ida (NGU)</li><li>Mercer, Jon (Ridge Uni)</li><li>Miller, Pia (NGU)</li><li>Moore, Seth (Eastvale)</li><li>Morrow, Kay (NGU)</li><li>Nash, Theo (Westmere)</li><li>Nolan, Amy (NGU)</li><li>North, Caleb (Coastal)</li><li>Oakley, Vera (NGU)</li><li>Ogden, Roy (Ridge Uni)</li><li>Page, Lily (NGU)</li><li>Parker, Ned (Eastvale)</li><li>Pearce, Gwen (NGU)</li><li>Perry, Max (Westmere)</li><li>Pike, Elsa (NGU)</li><li>Porter, Hal (Coastal)</li><li>Quinn, Ava (NGU)</li><li>Ramsay, Lou (NGU)</li></ul>
    <ul><li>Reed, Cleo (Eastvale)</li><li>Rhodes, Ian (NGU)</li><li>Riley, Joan (Ridge Uni)</li><li>Rowe, Eli (NGU)</li><li>Sadler, Fay (Coastal)</li><li>Sawyer, Jay (NGU)</li><li>Shaw, Meg (Westmere)</li><li>Sinclair, Tim (NGU)</li><li>Slater, Anya (Eastvale)</li><li>Snow, Carl (NGU)</li><li>Stone, Edie (Ridge Uni)</li><li>Sutton, Glen (NGU)</li><li>Talbot, Irene (Coastal)</li><li>Tate, Rowan (NGU)</li><li>Thorne, Ines (Eastvale)</li><li>Tovey, Mark (NGU)</li><li>Turner, Elle (Westmere)</li><li>Vance, Dale (NGU)</li><li>Vaughn, Ruby (Ridge Uni)</li><li>Wade, Kurt (NGU)</li></ul>
    <ul><li>Walsh, Nell (NGU)</li><li>Ward, Alec (Coastal)</li><li>Warren, Skye (NGU)</li><li>Watts, Doug (Eastvale)</li><li>Webb, Lorna (NGU)</li><li>West, Ezra (Ridge Uni)</li><li>Whelan, Kate (NGU)</li><li>White, Ross (Westmere)</li><li>Wilde, Sara (NGU)</li><li>Wills, Gabe (Coastal)</li><li>Wood, Tilly (NGU)</li><li>Wren, Hamish (Eastvale)</li><li>Wyatt, Opal (NGU)</li><li>Yates, Drew (Ridge Uni)</li><li>York, Bella (NGU)</li><li>Young, Clive (Westmere)</li><li>Yule, Fern (NGU)</li><li>Zane, Ollie (Coastal)</li><li>Zeller, Amy (NGU)</li><li>Zimmer, Lars (NGU)</li></ul>
  </div>
</section>

<footer class="footer">
  <div class="footer-brand">
    <span class="brand-mark"></span>
    <div class="brand-name">BRIGHT MEADOW<br>TEACHING<br>STANDARDS</div>
  </div>
  <div class="partner">
    <span class="partner-mark"></span>
    <p><strong>Northgate University</strong>Harbourside NSW 2150<br>Australia</p>
  </div>
  <div class="contact">
    <strong>Daniel Hargrove</strong>
    <span>National Teaching Fellow</span>
    <span>daniel.hargrove@northgate.edu.au</span>
    <span>+61(0)2 5550 1040</span>
  </div>
  <div class="contact">
    <strong>Claire Whitmore</strong>
    <span>Online Education Consultant</span>
    <span>claire.whitmore@northgate.edu.au</span>
    <span>+61(0)2 5550 4142</span>
  </div>
  <a class="site" href="http://www.brightmeadowhub.org">http://www.brightmeadowhub.org</a>
</footer>

</main>
</body>
</html>
```